lumen crest business card project

Financial consulting in line with life insurance ,index annuity, college funding solutions. I educate clients on cash flow, debt management, how to create emergency fund, how to proper protection with the best insurance, how to accummulate asset and management, how to preserve asset/ estate planning. Collge funding solutions help familes seek the best funding solutions possible including award letter review and test prep on ACT, SAT, PSAT, SAT II
Target Market(s)
Individuals, family, business
Industry/Entity Type
Financial Planning
Contact Information for Business Card
Business name: Lumen Crest Financial Services
Odell Vink
Managing Director
License no. 7K24316
Address: 2815 Tarlow Ave. Merrow Falls, CA 93482
Phone: 805-555-0148 Fax: 805-555-0193
Email: odell.vink@mailvora.com
Font styles to use
Other font styles liked:
- Bliss
Requirements
Must have
- Use feng shui as a guide to design the card make a flow curve lines only no angle or arrows.Size 3.5 inch by 2inch, metallic look is good, design a logo too . Keep it simple add image using feng shuis a guide. Also put a tagline that can make a very good impression. Use the back with something that the client we be able to use feng shui as guide.
Nice to have
- Use feng shui as guiding principle. Keep it simple
- Logo and tagline
Should not have
- Negative chi ,Angles, down ward design, too many things or too many images

```html
<!DOCTYPE html>
<html lang="en">
<head>
<meta charset="utf-8">
<title>Lumen Crest Financial Services – Business Card</title>
<link href="https://fonts.googleapis.com/css2?family=Cinzel:wght@400;600&family=Open+Sans:wght@400;600&display=swap" rel="stylesheet">
<style>
  :root {
    --bg: #e7e4e0;
    --steel-light: #c9cacb;
    --steel-mid: #9c9ea0;
    --steel-dark: #6f7173;
    --carbon-1: #3a3b3d;
    --carbon-2: #232426;
    --gunmetal-1: #4a4c4f;
    --gunmetal-2: #26272a;
    --ink: #1c1d1f;
    --text-light: #e9e9ea;
    --text-muted: #b4b5b7;
    --icon-bg: #e4e4e4;
    --icon-ink: #2a2b2d;
  }
  * { margin: 0; padding: 0; box-sizing: border-box; }
  html, body { width: 1200px; height: 800px; overflow: hidden; }
  body {
    background: var(--bg);
    position: relative;
    font-family: "Open Sans", sans-serif;
  }
  .card {
    position: absolute;
    border-radius: 6px;
    overflow: hidden;
    box-shadow: 0 14px 30px rgba(0,0,0,0.25);
  }
  .card-back {
    left: 90px; top: 180px;
    width: 250px; height: 437px;
    background: linear-gradient(160deg, var(--gunmetal-1), var(--gunmetal-2));
    display: flex; flex-direction: column; align-items: center; justify-content: center;
    gap: 14px;
  }
  .back-mark {
    width: 58px; height: 58px; border-radius: 50%;
    background: var(--ink);
  }
  .back-name {
    font-family: "Cinzel", serif; font-weight: 600;
    font-size: 22px; letter-spacing: 2px; color: var(--ink);
  }
  .card-front {
    left: 420px; top: 200px;
    width: 700px; height: 400px;
  }
  .surface { position: absolute; inset: 0; }
  .brand {
    position: absolute; left: 44px; top: 44px;
    display: flex; align-items: center; gap: 16px;
  }
  .brand-mark { width: 44px; height: 44px; border-radius: 50%; background: var(--ink); }
  .brand-name {
    font-family: "Cinzel", serif; font-weight: 600;
    font-size: 32px; letter-spacing: 1px; color: var(--ink); line-height: 1;
  }
  .brand-tag {
    font-family: "Cinzel", serif; font-weight: 600;
    font-size: 14px; letter-spacing: 2px; color: var(--ink); margin-top: 6px;
  }
  .office {
    position: absolute; left: 40px; top: 200px;
    font-style: normal;
    font-size: 13px; line-height: 1.55; color: var(--text-muted);
  }
  .person {
    position: absolute; right: 40px; top: 262px; text-align: right;
  }
  .person-name {
    font-family: "Cinzel", serif; font-weight: 600;
    font-size: 25px; letter-spacing: 1px; color: var(--text-light);
  }
  .person-title {
    font-size: 12px; letter-spacing: 1px; color: var(--text-muted); margin-bottom: 12px;
  }
  .contact { list-style: none; }
  .contact li {
    display: flex; justify-content: flex-end; align-items: center; gap: 10px;
    font-size: 13px; color: var(--text-light); line-height: 22px;
  }
  .contact-icon { width: 16px; height: 16px; flex: none; }
</style>
</head>
<body>

<section class="card card-back" aria-label="Card back">
  <span class="back-mark"></span>
  <span class="back-name">LUMEN CREST</span>
</section>

<section class="card card-front" aria-label="Card front">
  <svg class="surface" viewBox="0 0 700 400" preserveAspectRatio="none" aria-hidden="true">
    <defs>
      <linearGradient id="steel" x1="0" y1="0" x2="1" y2="1">
        <stop offset="0" stop-color="#c9cacb"/>
        <stop offset="0.55" stop-color="#9c9ea0"/>
        <stop offset="1" stop-color="#6f7173"/>
      </linearGradient>
      <linearGradient id="carbon" x1="0" y1="0" x2="1" y2="1">
        <stop offset="0" stop-color="#3a3b3d"/>
        <stop offset="1" stop-color="#232426"/>
      </linearGradient>
    </defs>
    <rect width="700" height="400" fill="url(#carbon)"/>
    <path d="M0,0 H700 V238 C520,160 260,120 0,128 Z" fill="#151617"/>
    <path d="M0,0 H700 V222 C520,148 260,110 0,118 Z" fill="url(#steel)"/>
  </svg>

  <div class="brand">
    <span class="brand-mark"></span>
    <div>
      <div class="brand-name">LUMEN CREST</div>
      <div class="brand-tag">FINANCIAL SERVICES</div>
    </div>
  </div>

  <address class="office">
    License no. 7K24316<br>
    2815 Tarlow Ave.<br>
    Merrow Falls, CA 93482
  </address>

  <div class="person">
    <div class="person-name">ODELL VINK</div>
    <div class="person-title">MANAGING DIRECTOR</div>
    <ul class="contact">
      <li>805-555-0148
        <svg class="contact-icon" viewBox="0 0 16 16" role="img" aria-label="Phone"><circle cx="8" cy="8" r="8" fill="#e4e4e4"/><path d="M5.2 4.2c.4-.3.9-.2 1.1.2l.6 1.2c.2.4 0 .7-.3.9l-.4.3c.3.9 1 1.6 1.9 1.9l.3-.4c.2-.3.6-.4.9-.3l1.2.6c.4.2.5.7.2 1.1-.6.8-1.6 1-2.5.5-1.7-.8-3-2.1-3.7-3.7-.4-.9-.1-1.9.7-2.3z" fill="#2a2b2d"/></svg>
      </li>
      <li>805-555-0193
        <svg class="contact-icon" viewBox="0 0 16 16" role="img" aria-label="Fax"><circle cx="8" cy="8" r="8" fill="#e4e4e4"/><rect x="5" y="4" width="6" height="3" fill="#2a2b2d"/><rect x="4" y="7" width="8" height="4" rx="1" fill="#2a2b2d"/><rect x="5.5" y="9.5" width="5" height="2.5" fill="#e4e4e4"/></svg>
      </li>
      <li>odell.vink@mailvora.com
        <svg class="contact-icon" viewBox="0 0 16 16" role="img" aria-label="Email"><circle cx="8" cy="8" r="8" fill="#e4e4e4"/><rect x="4" y="5" width="8" height="6" rx="1" fill="#2a2b2d"/><path d="M4.3 5.5 8 8.3l3.7-2.8" stroke="#e4e4e4" stroke-width="0.9" fill="none"/></svg>
      </li>
    </ul>
  </div>
</section>

</body>
</html>
```